Cedarbend Ridge Footraces

We need a website (wordpress) design for a new website that we will be launching. This is for a new trail racing series in Canada.
We recently had a logo designed so want to incorporate the colours of the logo on the website design. Especially the dark blue, green and orange.
Websites that we like for comparison of trail running race themes are:
https://www.mossyboulderrunning.example/
https://www.quillpathcircuit.example/
http://www.tidecovecircuit.example/
https://www.amberfellcircuit.example/
http://www.brookmarchrunseries.example/

Target Market(s)

Outdoor trail runners

Coding

Coded - Design and coding required

Number of Pages Required

4 page

Font styles to use
Sans Serif

Colors
0255a3
33b8a4
f37122

Requirements
Must have
• There will be a main page with eye catching design noting what we do. Page 2 and 3 will be for each race in the series. Page 1 will be a specific race, and page 2 with be for another race. page 3 and 4 will be for future races that we add so that each race has their own page.
• Our races all take place in the mountains, so using graphics including mountains, rivers, trees is all a requirement for us.
• Our logo is attached, we want to use the colours of the logo in the website design.
Nice to have
• Outdoor theme is a nice to have. We like wood and earth tone colours, and pictures/graphics of runners and mountains and trees.
• There are 4 people involved in our organization. We'd like a photo and brief blurb of each of us, similar to how this website did their layout: https://www.mossyboulderrunning.example/

```html
<!DOCTYPE html>
<html lang="en">
<head>
<meta charset="utf-8">
<title>Cedarbend Ridge Footraces</title>
<link href="https://fonts.googleapis.com/css2?family=Montserrat:wght@300;400;700;800&family=Permanent+Marker&display=swap" rel="stylesheet">
<style>
  :root {
    --forest-dark: #16200f;
    --forest-mid: #2f3d1c;
    --earth: #5a4a36;
    --white: #ffffff;
    --orange: #f39a12;
    --blue-deep: #0d6b94;
    --blue-text: #2a86a8;
    --sunset: #e7b25c;
    --river: #4f5a3c;
    --sky: #9fc8d8;
  }
  * { margin: 0; padding: 0; box-sizing: border-box; }
  html, body { width: 1200px; height: 1200px; overflow: hidden; background: var(--white); }
  body { position: relative; font-family: "Montserrat", Arial, sans-serif; }

  .hero {
    position: absolute; left: 0; top: 0; width: 1200px; height: 622px;
    background:
      radial-gradient(ellipse at 60% 85%, rgba(120,100,78,.75) 0%, rgba(90,74,54,.4) 30%, transparent 55%),
      radial-gradient(ellipse at 20% 30%, #3c5224 0%, transparent 50%),
      radial-gradient(ellipse at 85% 40%, #44592a 0%, transparent 45%),
      linear-gradient(180deg, var(--forest-mid) 0%, var(--forest-dark) 55%, var(--earth) 100%);
    clip-path: polygon(0 0, 100% 0, 100% 621px, 0 587px);
  }

  .site-nav {
    position: absolute; top: 34px; left: 84px; right: 86px;
    display: flex; align-items: center; justify-content: space-between;
    color: var(--white); font-weight: 800; letter-spacing: .4px;
  }
  .site-nav .brand { font-size: 17px; }
  .site-nav ul { list-style: none; display: flex; gap: 43px; font-size: 15px; }

  .hero-brand {
    position: absolute; left: 96px; top: 250px; width: 160px;
    text-align: center; color: var(--white);
    font-weight: 800; font-size: 29px; line-height: 1.02; text-transform: uppercase;
  }
  .hero-rule { position: absolute; left: 331px; top: 180px; width: 4px; height: 266px; background: var(--orange); border-radius: 2px; }
  .hero-title {
    position: absolute; left: 388px; top: 248px; width: 720px;
    font-family: "Permanent Marker", "Arial Black", sans-serif;
    color: var(--white); font-size: 52px; line-height: 68px; font-weight: 400;
    text-transform: uppercase; letter-spacing: -.5px;
  }
  .scroll-cue { position: absolute; left: 569px; top: 517px; }

  .about { position: absolute; left: 110px; top: 700px; width: 980px; text-align: center; }
  .about h2 { color: var(--blue-deep); font-weight: 800; font-size: 27px; letter-spacing: 1px; margin-bottom: 10px; }
  .about p { color: var(--blue-text); font-weight: 300; font-size: 18px; line-height: 30px; }
  .about strong { color: var(--blue-deep); font-weight: 800; }

  .race-photo { position: absolute; top: 1111px; height: 89px; }
  .race-photo.sunset { left: 0; width: 313px; background: linear-gradient(180deg, #f6e6c7 0%, var(--sunset) 60%, #b9773a 100%); }
  .race-photo.bridge { left: 333px; width: 535px; background: linear-gradient(90deg, #2e3a22 0%, var(--river) 40%, #9a9a88 50%, var(--river) 60%, #26331c 100%); }
  .race-photo.peaks { left: 886px; width: 314px; background: linear-gradient(180deg, #d8ecf4 0%, var(--sky) 55%, #5f8ea6 100%); }
</style>
</head>
<body>
  <section class="hero" role="img" aria-label="Two trail runners with poles climbing a dirt path through a dark green forest"></section>

  <nav class="site-nav">
    <div class="brand">CEDARBEND RIDGE FOOTRACES</div>
    <ul>
      <li>HOME</li>
      <li>RACE ONE</li>
      <li>RACE TWO</li>
      <li>FUTURE RACES</li>
      <li>REGISTER</li>
    </ul>
  </nav>

  <div class="hero-brand">Cedarbend Ridge Footraces</div>
  <div class="hero-rule"></div>
  <h1 class="hero-title">Join us in the greatest race through the mountains ever run</h1>

  <svg class="scroll-cue" width="62" height="62" viewBox="0 0 62 62" aria-label="Scroll down">
    <circle cx="31" cy="31" r="28" fill="none" stroke="#f39a12" stroke-width="3"/>
    <path d="M31 8 V46 M20 34 L31 46 L42 34" fill="none" stroke="#f39a12" stroke-width="3" stroke-linecap="round" stroke-linejoin="round"/>
  </svg>

  <section class="about">
    <h2>ABOUT OUR RACES</h2>
    <p>Welcome to the <strong>CEDARBEND RIDGE FOOTRACE</strong> Series where we host a variety of grass-roots events in beautiful British Columbia.&nbsp; Our goal is simple.&nbsp; To offer challenging &amp; scenic race courses that leave our participants feeling exhausted but overjoyed upon completion.&nbsp; We also support local charities in the process.&nbsp; We call it the 'share the love' program.&nbsp; Basically what that means is we create outstanding and memorable courses on some of our favorite trails that include as much climbing and single track as we can find.&nbsp; Then we donate a portion of each race entry back to organizations in need.&nbsp; Yea, our races are hard.&nbsp; All of them... But don't let that psych you out.&nbsp; Every year we witness people from all over who cross the finish line with huge smiles, wobbly legs and where we embrace sweaty hugs + reward our racers with handmade finishers medals made with more "love".&nbsp; Plus your participation helps us give back!</p>
  </section>

  <div class="race-photo sunset" role="img" aria-label="Mountain ridge silhouetted against a golden sunset"></div>
  <div class="race-photo bridge" role="img" aria-label="Aerial view of a suspension bridge over a forested river canyon"></div>
  <div class="race-photo peaks" role="img" aria-label="Snow-capped mountain range under a pale blue sky"></div>
</body>
</html>
```